Fire and Building compliance company needs website

A professional website is needed for Kestow Alarm and Guard 2012 , company profile attached- we have a website but it is old and needs replacing (in fact we can not access it at present).

We are also looking at getting logo redesigned and will probably change to a flame type graphic with the letters KAG and then Fire and Building Compliance (bellow KAG).

It Company

• Ease of use
Page should fit inside typical screen size (not have to scroll down to see page).
Be made in Joomla 2.5

search words- Wanganui, fire alarm, building compliance, building warrant of fitness,BWOF, burglar alarm systems, LPG refilling,fire extinguishers, emergency lighting.

```html
<!DOCTYPE html>
<html lang="en">
<head>
<meta charset="utf-8">
<title>Kestow Alarm &amp; Guard</title>
<link rel="stylesheet" href="https://fonts.googleapis.com/css2?family=PT+Sans:wght@400;700&family=PT+Sans+Narrow:wght@400;700&family=Fira+Sans+Extra+Condensed:ital,wght@1,300&display=swap">
<style>
  :root {
    --dark: #2a2a2a;
    --red: #d92127;
    --red-light: #e8454a;
    --accent: #e0312f;
    --band: #f1f0f0;
    --line: #d6d6d6;
    --text: #333333;
    --white: #ffffff;
  }
  * { margin: 0; padding: 0; box-sizing: border-box; }
  html, body { width: 1200px; height: 1020px; overflow: hidden; background: var(--white); }
  body { position: relative; font-family: "PT Sans Narrow", "Arial Narrow", sans-serif; color: var(--text); }

  .site-header { position: absolute; top: 0; left: 0; width: 1200px; height: 66px; background: var(--dark); border-bottom: 1px solid #111; }
  .brand { position: absolute; left: 150px; top: 10px; display: flex; align-items: center; gap: 12px; }
  .brand-mark { width: 40px; height: 40px; border-radius: 50%; background: var(--accent); }
  .brand-name { font-family: "PT Sans", sans-serif; font-weight: 700; font-size: 19px; line-height: 21px; color: var(--white); text-transform: uppercase; }
  .main-nav { position: absolute; top: 26px; left: 544px; display: flex; font-size: 13px; text-transform: uppercase; letter-spacing: 0.3px; }
  .main-nav a { color: #e6e6e6; text-decoration: none; }
  .main-nav a.active { color: var(--accent); }
  .main-nav a:nth-child(1) { margin-right: 37px; }
  .main-nav a:nth-child(2) { margin-right: 40px; }
  .main-nav a:nth-child(3) { margin-right: 40px; }
  .main-nav a:nth-child(4) { margin-right: 35px; }
  .main-nav a:nth-child(5) { margin-right: 40px; }

  .hero { position: absolute; top: 67px; left: 0; width: 1200px; height: 332px;
    background: radial-gradient(ellipse at 40% 85%, var(--red-light) 0%, var(--red) 55%, #c81a20 100%); }
  .hero-kicker { position: absolute; left: 119px; top: 53px; font-family: "PT Sans", sans-serif; font-size: 20px; color: #2a1414; }
  .hero-title { position: absolute; left: 117px; top: 83px; font-family: "PT Sans", sans-serif; font-weight: 700; font-size: 49px; color: var(--white); letter-spacing: -0.3px; }
  .hero-copy { position: absolute; left: 120px; top: 152px; width: 540px; font-family: "PT Sans", sans-serif; font-weight: 700; font-size: 14.5px; line-height: 22px; color: var(--white); }
  .btn-dark { position: absolute; left: 120px; top: 243px; width: 199px; height: 39px; background: var(--dark); color: var(--white); font-size: 16px; text-transform: uppercase; text-align: center; line-height: 39px; letter-spacing: 0.5px; padding-right: 10px; }
  .hero-art { position: absolute; left: 690px; top: 28px; width: 450px; height: 304px;
    background: radial-gradient(ellipse at 50% 70%, #f7c64a 0%, #f08a2a 35%, rgba(232,80,40,0.4) 65%, rgba(217,33,39,0) 80%); }

  .signup { position: absolute; top: 399px; left: 0; width: 1200px; height: 73px; background: var(--band); border-top: 2px solid #c9c9c9; border-bottom: 1px solid var(--line); }
  .signup-title { position: absolute; left: 122px; top: 18px; font-family: "Fira Sans Extra Condensed", sans-serif; font-style: italic; font-weight: 300; font-size: 25px; letter-spacing: -0.2px; color: var(--red); white-space: nowrap; }
  .signup-input { position: absolute; left: 453px; top: 18px; width: 261px; height: 32px; background: var(--white); border: 1px solid #cfcfcf; font-style: italic; font-size: 13px; color: #888; padding: 7px 10px; }
  .signup-go { position: absolute; left: 720px; top: 18px; width: 46px; height: 32px; background: var(--dark); color: var(--white); font-size: 16px; text-align: center; line-height: 30px; border: 1px solid #bbb; }

  .intro { position: absolute; left: 121px; top: 484px; width: 940px; font-size: 15px; letter-spacing: 0.35px; line-height: 24px; color: var(--text); }
  .intro p + p { margin-top: 24px; }

  .feature { position: absolute; top: 630px; width: 256px; }
  .feature-frame { width: 256px; height: 153px; background: var(--white); border: 1px solid #e2e2e2; box-shadow: 0 1px 3px rgba(0,0,0,0.12); padding: 12px; }
  .feature-photo { width: 230px; height: 127px; }
  .photo-alarm { background: linear-gradient(180deg, #f03a3a, #c21e22); }
  .photo-smoke { background: linear-gradient(180deg, #8fb3d8 0%, #b9b5ae 45%, #6a6150 75%, #4f6a2f 100%); }
  .photo-wiring { background: linear-gradient(90deg, #5a4a3a 0%, #c8c4bc 40%, #d49a40 75%, #c8772c 100%); }
  .feature-text { margin-top: 20px; padding-left: 2px; width: 256px; font-size: 15px; letter-spacing: 0.35px; line-height: 24px; color: var(--text); }
  .feature-link { display: block; margin-top: 9px; padding-left: 2px; font-size: 13px; color: var(--red); text-decoration: none; }

  .site-footer { position: absolute; top: 945px; left: 0; width: 1200px; height: 75px; background: var(--dark); }
  .footer-nav { position: absolute; left: 121px; top: 32px; display: flex; font-size: 11.5px; font-weight: 700; text-transform: uppercase; }
  .footer-nav a { color: #f0f0f0; text-decoration: none; }
  .footer-nav a.active { color: var(--accent); }
  .footer-nav a:nth-child(1) { margin-right: 31px; }
  .footer-nav a:nth-child(2) { margin-right: 34px; }
  .footer-nav a:nth-child(3) { margin-right: 34px; }
  .footer-nav a:nth-child(4) { margin-right: 29px; }
  .footer-nav a:nth-child(5) { margin-right: 35px; }
  .social { position: absolute; left: 630px; top: 26px; display: flex; gap: 21px; }
  .social-square { width: 25px; height: 25px; border-radius: 3px; }
  .sq-a { background: #3aa7c9; }
  .sq-b { background: #3b64a8; }
  .sq-c { background: #f08a1e; }
  .sq-d { background: #3a79b8; }
  .copyright { position: absolute; right: 120px; top: 32px; font-size: 11px; color: var(--accent); text-transform: uppercase; }
  .copyright strong { color: var(--white); }
</style>
</head>
<body>
  <header class="site-header">
    <div class="brand">
      <span class="brand-mark"></span>
      <span class="brand-name">Kestow<br>Alarm &amp; Guard</span>
    </div>
    <nav class="main-nav">
      <a class="active" href="#">Home</a>
      <a href="#">What we do</a>
      <a href="#">Who we are</a>
      <a href="#">Services</a>
      <a href="#">Products</a>
      <a href="#">Contact us</a>
    </nav>
  </header>

  <section class="hero">
    <p class="hero-kicker">Proin vehicula pulvinar nisi ac semper terrting elering</p>
    <h1 class="hero-title">EXPERIENCE IN FIRE SAFETY</h1>
    <p class="hero-copy">Lorem ipsum dolor sit amet, consectetur adipiscing elit. Praesent dolor nunc, rhoncus porttitor bibendum in, placerat sed dui raesent suscipit consequat nunc, et accumsan arcu erintng ojkofj mkdoing seerlto.</p>
    <a class="btn-dark">Read more</a>
    <div class="hero-art" role="img" aria-label="Two figures in hard hats holding a drill and toolbox in front of flames"></div>
  </section>

  <section class="signup">
    <h2 class="signup-title">Sign up for latest news and offers</h2>
    <div class="signup-input">enter your email</div>
    <div class="signup-go">GO</div>
  </section>

  <section class="intro">
    <p>Kestow Alarm &amp; Guard is a locally owned and operated fire protection company.&nbsp; Since 1978 we have evolved and developed to suit the demands of our clients and the 1992 Building Compliance Act.&nbsp; This ability to alter and change as required means that we are now viewed as an innovative and contemporary company.</p>
    <p>Our Managing Director Dean Kestow formed the company and has now worked in the fire industry for 30 years.&nbsp; Dean Kestow is an approved Skillmark registered accessor.</p>
  </section>

  <article class="feature" style="left:119px">
    <div class="feature-frame"><div class="feature-photo photo-alarm" role="img" aria-label="Red fire alarm break glass call point"></div></div>
    <p class="feature-text">Our Managing Director Dean Kestow formed the company and has now worked in the fire industry for 30 years.</p>
    <a class="feature-link" href="#">read more &gt;</a>
  </article>
  <article class="feature" style="left:471px">
    <div class="feature-frame"><div class="feature-photo photo-smoke" role="img" aria-label="Smoke rising from a burning building under blue sky"></div></div>
    <p class="feature-text">Our Managing Director Dean Kestow formed the company and has now worked in the fire industry for 30 years.</p>
    <a class="feature-link" href="#">read more &gt;</a>
  </article>
  <article class="feature" style="left:821px">
    <div class="feature-frame"><div class="feature-photo photo-wiring" role="img" aria-label="Technician wiring a fire alarm control panel"></div></div>
    <p class="feature-text">Our Managing Director Dean Kestow formed the company and has now worked in the fire industry for 30 years.</p>
    <a class="feature-link" href="#">read more &gt;</a>
  </article>

  <footer class="site-footer">
    <nav class="footer-nav">
      <a class="active" href="#">Home</a>
      <a href="#">What we do</a>
      <a href="#">Who we are</a>
      <a href="#">Services</a>
      <a href="#">Products</a>
      <a href="#">Contact us</a>
    </nav>
    <div class="social">
      <span class="social-square sq-a"></span>
      <span class="social-square sq-b"></span>
      <span class="social-square sq-c"></span>
      <span class="social-square sq-d"></span>
      <svg width="25" height="25" viewBox="0 0 25 25" aria-label="Email">
        <rect x="0.5" y="4.5" width="24" height="16" rx="1.5" fill="#f4f4f4" stroke="#bbb"/>
        <path d="M1 5.5 L12.5 14 L24 5.5" fill="none" stroke="#aaa" stroke-width="1.2"/>
      </svg>
    </div>
    <p class="copyright">Copyright 2012 <strong>Allrights reserved</strong></p>
  </footer>
</body>
</html>
```